amber crest health and wellness group.

need a full website design , all information provided in word document labeled website blue print

Target Market(s)

first responders, military , people in crisis

Coding

Coded - Design and coding required

Number of Pages Required

1 page

```html
<!DOCTYPE html>
<html lang="en">
<head>
<meta charset="utf-8">
<title>Amber Crest Health &amp; Wellness Group</title>
<link rel="stylesheet" href="https://fonts.googleapis.com/css2?family=Figtree:wght@500;600;700&family=Montserrat:wght@400;500;600&display=swap">
<style>
:root{
  --blue:#2b5d9c;
  --blue-deep:#244f86;
  --ink:#1b1b1b;
  --body:#3a3a3a;
  --nav-bg:#ececec;
  --hero-dark:#141414;
  --grey-band:#a7a7a7;
  --soft:#f4f5f7;
  --white:#ffffff;
}
*{margin:0;padding:0;box-sizing:border-box}
html,body{width:1200px;height:2861px;overflow:hidden;background:var(--white)}
body{position:relative;font-family:"Montserrat",sans-serif;color:var(--body)}
.abs{position:absolute}
h1,h2,h3{font-family:"Figtree",sans-serif;font-weight:600;color:var(--ink)}
.btn{position:absolute;display:flex;align-items:center;justify-content:center;border-radius:16px;font-size:10px;letter-spacing:.4px;text-transform:uppercase;font-weight:500}
.btn-solid{background:var(--blue);color:var(--white)}
.btn-line{border:1px solid var(--blue);color:var(--blue)}

/* header */
.site-header{position:absolute;left:0;top:0;width:1200px;height:62px;background:var(--nav-bg);z-index:3}
.brand{position:absolute;left:193px;top:0;width:124px;height:102px;background:#161616;display:flex;flex-direction:column;align-items:center;justify-content:center;gap:6px;z-index:4}
.brand-mark{width:20px;height:20px;border-radius:50%;background:var(--blue)}
.brand-name{font-family:"Montserrat",sans-serif;font-size:9px;font-weight:600;color:var(--blue);text-align:center;line-height:1.2;text-transform:uppercase}
.main-nav{position:absolute;left:390px;top:24px;display:flex;gap:31px;font-size:10.5px;color:#333;text-transform:uppercase}
.main-nav .active{color:var(--blue);position:relative}
.main-nav .active::after{content:"";position:absolute;left:0;right:0;top:34px;height:2px;background:var(--blue)}
.nav-contact{left:906px;top:16px;width:100px;height:31px}

/* hero */
.hero{position:absolute;left:0;top:62px;width:1200px;height:588px;background:linear-gradient(100deg,#0e0e0e 0%,#1c1c1c 45%,#3a2f28 70%,#1a1a1a 100%)}
.hero-title{position:absolute;left:193px;top:194px;font-size:43px;line-height:49px;color:var(--white);letter-spacing:.5px;font-weight:700}
.hero-text{position:absolute;left:194px;top:295px;width:440px;font-size:13.5px;line-height:19px;color:#e6e6e6}
.hero .btn-line{border-color:var(--blue);color:#8fb0da}
.scroll-cue{position:absolute;left:194px;top:559px;width:24px;height:53px;border:1.5px solid var(--white);border-radius:12px}

/* about */
.about-photo{position:absolute;left:193px;top:702px;width:373px;height:448px;background:linear-gradient(135deg,#6f5444,#c9a894 45%,#8aa4c8 70%,#b98e72)}
.about-frame{position:absolute;left:219px;top:728px;width:371px;height:448px;border:1px solid var(--blue)}
.eyebrow{position:absolute;left:636px;top:728px;font-size:10px;letter-spacing:2px;font-weight:600;color:var(--blue)}
.about-title{position:absolute;left:635px;top:750px;font-size:29px;line-height:30px}
.about-title span{color:var(--blue)}
.rule{position:absolute;height:1px;background:var(--blue)}
.copy{position:absolute;font-size:10.5px;line-height:17.5px;color:var(--body)}

/* services */
.services{position:absolute;left:0;top:1238px;width:1200px;height:358px;background:linear-gradient(90deg,#eeeceb,#f3f2f1 50%,#ecebea)}
.services-tail{position:absolute;left:0;top:1596px;width:400px;height:53px;background:#efeeed}
.services h2{position:absolute;left:193px;top:1294px;font-size:27px}
.arrow-btn{position:absolute;top:1296px;width:31px;height:31px;border-radius:50%}
.card-img{position:absolute;top:1344px;width:194px;height:150px}
.card-label{position:absolute;top:1505px;width:190px;font-size:12px;line-height:15px;font-weight:500;color:var(--ink)}

/* mission */
.mv-heading{position:absolute;left:193px;top:1706px;font-size:27px}
.mv-img{position:absolute;top:1757px;width:335px;height:163px}
.mv-strip{position:absolute;top:1920px;width:63px;height:63px}
.mv-title{position:absolute;top:1935px;font-size:20px;font-weight:500}
.mv-line-v{position:absolute;top:1994px;width:1px;height:87px;background:var(--blue)}
.mv-line-h{position:absolute;top:2080px;width:87px;height:1px;background:var(--blue)}

/* partners */
.partners{position:absolute;left:0;top:2144px;width:1200px;height:232px;background:var(--soft)}
.partners h2{position:absolute;left:0;width:1200px;top:2200px;text-align:center;font-size:27px}
.badge{position:absolute;top:2256px;width:126px;height:56px;background:var(--white);border:1px solid #e6e6e6}
.badge i{position:absolute;left:28px;top:18px;width:70px;height:20px;border-radius:10px;background:#d9dfe8}

/* cta */
.cta{position:absolute;left:0;top:2376px;width:1200px;height:485px;background:linear-gradient(180deg,#2d62a4,#2a5c9d)}
.cta-title{position:absolute;left:0;width:1200px;top:2522px;text-align:center;font-size:51px;line-height:58px;color:var(--white);font-weight:700}
.cta .btn-line{border-color:#fff;color:#fff}
.foot-line{position:absolute;left:193px;width:813px;height:1px;background:rgba(255,255,255,.55)}
.foot-nav{position:absolute;left:192px;top:2777px;width:816px;display:flex;justify-content:space-between;font-size:11.5px;color:#fff;text-transform:uppercase}
.foot-nav .active{font-weight:600}
.copyright{position:absolute;left:0;width:1200px;top:2823px;text-align:center;font-size:10.5px;color:#fff}
.copyright span{text-decoration:underline}
</style>
</head>
<body>

<header class="site-header">
  <nav class="main-nav">
    <span class="active">Home</span><span>About Us</span><span>Services &#8964;</span><span>Our Team</span><span>Mission &amp; Vision</span><span>FAQ'S</span>
  </nav>
  <a class="btn btn-solid nav-contact">Contact Us</a>
</header>
<div class="brand"><span class="brand-mark"></span><span class="brand-name">Amber Crest<br>Health &amp; Wellness</span></div>

<section class="hero" role="img" aria-label="Therapist giving a massage to a client lying face down in a dim room"></section>
<h1 class="hero-title abs">HELPING THOSE<br>WHO HELP OTHERS</h1>
<p class="hero-text">Lorem ipsum dolor sit amet, consectetur adipiscing elit, sed do eiusmod tempor incididunt ut labore et dolore magna aliqua.</p>
<a class="btn btn-solid" style="left:194px;top:352px;width:100px;height:30px">Inquiry Now!</a>
<a class="btn btn-line" style="left:307px;top:352px;width:100px;height:30px">Join Now!</a>
<div class="scroll-cue"><svg width="21" height="50" viewBox="0 0 21 50"><path d="M10.5 16v18M5.5 29l5 5 5-5" stroke="#fff" stroke-width="1.6" fill="none"/></svg></div>
<svg class="abs" style="left:0;top:610px" width="1200" height="40" viewBox="0 0 1200 40">
  <polygon points="0,34 1200,2 1200,24 0,34" fill="var(--blue)"/>
  <polygon points="0,34 1200,24 1200,40 0,40" fill="var(--grey-band)"/>
</svg>

<div class="about-frame"></div>
<div class="about-photo" role="img" aria-label="Salt scrub treatment on a relaxed client's shoulder"></div>
<span class="eyebrow">ABOUT US</span>
<h2 class="about-title">Welcome To The<br><span>Amber Crest Health &amp; Wellness<br>Group</span></h2>
<div class="rule" style="left:636px;top:848px;width:60px"></div>
<p class="copy" style="left:633px;top:863px;width:375px">Lorem ipsum dolor sit amet, consectetur adipiscing elit, sed do eiusmod tempor incididunt ut labore et dolore magna aliqua. Quis ipsum suspendisse ultrices gravida. Risus commodo viverra maecenas accumsan lacus vel facilisis.</p>
<p class="copy" style="left:633px;top:950px;width:375px">Lorem ipsum dolor sit amet, consectetur adipiscing elit, sed do eiusmod tempor incididunt ut labore et dolore magna aliqua. Quis ipsum suspendisse ultrices gravida. Risus commodo viverra maecenas accumsan lacus vel facilisis. Lorem ipsum dolor sit amet, consectetur adipiscing elit, sed do eiusmod tempor incididunt ut labore et dolore magna aliqua. Quis ipsum suspendisse ultrices gravida. Risus commodo viverra maecenas accumsan lacus vel facilisis.</p>
<a class="btn btn-solid" style="left:633px;top:1092px;width:100px;height:31px">Read More</a>
<a class="btn btn-line" style="left:746px;top:1092px;width:100px;height:31px">Inquiry Now!</a>

<section class="services" role="img" aria-label="Soft, faded photo of a counselling session"></section>
<div class="services-tail"></div>
<h2>Our Services</h2>
<svg class="arrow-btn" style="left:936px" viewBox="0 0 31 31"><circle cx="15.5" cy="15.5" r="14.8" fill="none" stroke="var(--blue)"/><path d="M20 15.5H11M14 12.5l-3 3 3 3" stroke="var(--blue)" fill="none" stroke-width="1.3"/></svg>
<svg class="arrow-btn" style="left:974px" viewBox="0 0 31 31"><circle cx="15.5" cy="15.5" r="15.5" fill="var(--blue)"/><path d="M11 15.5h9M17 12.5l3 3-3 3" stroke="#fff" fill="none" stroke-width="1.3"/></svg>
<div class="card-img" style="left:193px;background:linear-gradient(135deg,#b9ada0,#5d5a52)" role="img" aria-label="Counsellor holding hands with a young client"></div>
<div class="card-img" style="left:400px;background:linear-gradient(135deg,#c7cfd8,#b4352d 60%,#5c6470)" role="img" aria-label="Paramedics in red uniforms inside an ambulance"></div>
<div class="card-img" style="left:606px;background:linear-gradient(135deg,#3a2418,#8b5a40)" role="img" aria-label="Hands applying salt scrub on a back"></div>
<div class="card-img" style="left:812px;background:linear-gradient(135deg,#6d6a2c,#c59a5c 55%,#3b3a20)" role="img" aria-label="Client lying beside singing bowls"></div>
<div class="card-img" style="left:1019px;width:181px;background:linear-gradient(135deg,#f3d9cf,#e8b8a6);opacity:.6" role="img" aria-label="Client wearing a red-light therapy mask"></div>
<span class="card-label" style="left:193px">Mental Health Therapy</span>
<span class="card-label" style="left:400px">Trauma &amp; First Responder Support</span>
<span class="card-label" style="left:606px">Salt Therapy</span>
<span class="card-label" style="left:812px">Sound &amp; Vibration Therapy</span>
<span class="card-label" style="left:1019px;color:#9a9a9a">Red-Light Therapy</span>
<a class="btn btn-line" style="left:193px;top:1556px;width:140px;height:31px">View All Services</a>

<h2 class="mv-heading">Mission &amp; Vision</h2>
<div class="mv-img" style="left:193px;background:linear-gradient(135deg,#6c737b,#b8442f 45%,#3c4450)" role="img" aria-label="Paramedics treating a patient in an ambulance"></div>
<div class="mv-strip" style="left:193px;background:#3f444b"></div>
<h3 class="mv-title" style="left:279px">Mission</h3>
<div class="rule" style="left:281px;top:1965px;width:38px"></div>
<p class="copy" style="left:280px;top:1982px;width:290px">Lorem ipsum dolor sit amet, consectetur adipiscing elit, sed do eiusmod tempor incididunt ut labore et dolore magna aliqua. Quis ipsum suspendisse ultrices gravida. Risus commodo viverra maecenas accumsan lacus vel facilisis.</p>
<div class="mv-line-v" style="left:589px"></div><div class="mv-line-h" style="left:503px"></div>

<div class="mv-img" style="left:609px;background:linear-gradient(135deg,#b7b2ab,#6f8fb4 55%,#1f4f80)" role="img" aria-label="Clinician fitting an EEG cap on a patient beside brain scan screens"></div>
<div class="mv-strip" style="left:609px;background:#2f3338"></div>
<h3 class="mv-title" style="left:694px">Vision</h3>
<div class="rule" style="left:696px;top:1965px;width:38px"></div>
<p class="copy" style="left:695px;top:1982px;width:290px">Lorem ipsum dolor sit amet, consectetur adipiscing elit, sed do eiusmod tempor incididunt ut labore et dolore magna aliqua. Quis ipsum suspendisse ultrices gravida. Risus commodo viverra maecenas accumsan lacus vel facilisis.</p>
<div class="mv-line-v" style="left:1005px"></div><div class="mv-line-h" style="left:919px"></div>

<section class="partners"></section>
<h2 style="position:absolute;left:0;width:1200px;top:2200px;text-align:center;font-size:27px">Community Partners</h2>
<div class="badge" style="left:-30px"><i></i></div>
<div class="badge" style="left:108px"><i></i></div>
<div class="badge" style="left:248px"><i></i></div>
<div class="badge" style="left:387px"><i></i></div>
<div class="badge" style="left:526px"><i></i></div>
<div class="badge" style="left:666px"><i></i></div>
<div class="badge" style="left:805px"><i></i></div>
<div class="badge" style="left:944px"><i></i></div>
<div class="badge" style="left:1084px"><i></i></div>

<section class="cta" role="img" aria-label="Blue-tinted photo of a patient receiving care"></section>
<h2 class="cta-title">Ready to Transform<br>Your Scheduling?</h2>
<a class="btn btn-line" style="left:528px;top:2658px;width:144px;height:39px;border-radius:20px;font-size:12px">Inquiry Now!</a>
<div class="foot-line" style="top:2760px"></div>
<nav class="foot-nav"><span class="active">Home</span><span>About Us</span><span>Our Services</span><span>Our Team</span><span>Mission &amp; Vision</span><span>FAQ'S</span><span>Contact Us</span></nav>
<div class="foot-line" style="top:2807px"></div>
<p class="copyright">Copyright © 2025 <span>Amber Crest Health &amp; Wellness Group</span>. All Rights Reserved</p>

</body>
</html>
```